Fresh pet feed direct from manufacturer to door step. Quality and Freshness un-surpassed in Industr

Need Business Card Design; leading into many other projects, for New Franchised Business Opportunity providing home delivery of fresh dog and cat feed (no emphasis needed for cat) direct from manufacturing facility. (no middle men or distributors) Food is Farm to Factory fresh. Our trademarked tagline is "Freshness is our FIRST Promise ! "
Updates

Please take note of other contest for Chirplane Cover and Profile Pic's

Target Market(s)

Dog and Cat owners

Industry/Entity Type

Pet

Contact Information for Business Card

Name, address, local phone, national 800 number, website, email address

Other font styles liked:
• follow that from logo

Requirements
Must have
• Our feed is made in Texas with ingredients sourced from local farms. We want to lean heavy on the Made in West Texas , ranch theme but that has a 'black label', 'vantrel', 'premium', 'high-end' look and feel
Nice to have
• maybe have an offer on card? 20% off with promo code "x" etc.. ?? just a thought...

```html
<!DOCTYPE html>
<html lang="en">
<head>
<meta charset="utf-8">
<title>Ranger's Premium — Business Card</title>
<link href="https://fonts.googleapis.com/css2?family=Barlow:wght@400;600;700&display=swap" rel="stylesheet">
<style>
  :root {
    --stage: #9a9a9a;
    --black: #121212;
    --black-soft: #262626;
    --gold: #c8962a;
    --gold-deep: #a9741a;
    --white: #f4f1ea;
  }
  * { box-sizing: border-box; margin: 0; padding: 0; }
  html, body { width: 1200px; height: 720px; overflow: hidden; }
  body {
    background: var(--stage);
    font-family: "Barlow", Arial, sans-serif;
    display: flex;
    align-items: center;
    justify-content: center;
    gap: 40px;
  }
  .card {
    position: relative;
    width: 540px;
    height: 310px;
    overflow: hidden;
    box-shadow: 0 6px 18px rgba(0,0,0,.35);
  }
  .card-front { background: linear-gradient(100deg, var(--black) 0%, var(--black-soft) 55%, var(--black) 100%); }
  .card-back { background: linear-gradient(120deg, var(--gold) 0%, var(--gold-deep) 100%); }
  .card-art { position: absolute; inset: 0; }

  .brand {
    position: absolute;
    display: flex;
    align-items: center;
    gap: 10px;
    font-weight: 600;
    letter-spacing: .06em;
    text-transform: uppercase;
    white-space: nowrap;
    font-size: 28px;
  }
  .brand-dot { width: 14px; height: 14px; border-radius: 50%; background: currentColor; }
  .card-front .brand { left: 150px; top: 60px; color: var(--white); }
  .card-back .brand { left: 70px; top: 72px; color: var(--black); }

  .tagline {
    position: absolute;
    left: 70px; top: 128px;
    font-size: 15px;
    letter-spacing: .03em;
    color: var(--white);
  }

  .name-band {
    position: absolute;
    left: 280px; top: 150px;
    width: 260px; height: 58px;
    background: var(--gold);
    padding: 10px 24px 0 30px;
    text-align: right;
  }
  .person-name { font-size: 18px; font-weight: 700; letter-spacing: .14em; color: var(--black); }
  .person-role { font-size: 14px; letter-spacing: .12em; color: var(--black); margin-top: 2px; }
  .band-rule { position: absolute; left: 250px; width: 290px; height: 2px; background: var(--gold); }

  .contact {
    position: absolute;
    right: 22px; top: 226px;
    list-style: none;
    color: var(--white);
    font-size: 12.5px;
    letter-spacing: .1em;
    line-height: 15px;
    text-align: right;
  }
  .contact li { display: flex; justify-content: flex-end; align-items: center; gap: 8px; white-space: nowrap; }
  .contact-icon { width: 12px; height: 12px; fill: var(--white); flex: none; }
  .contact-icon.blank { fill: none; }
</style>
</head>
<body>

<section class="card card-front" aria-label="Business card front">
  <svg class="card-art" viewBox="0 0 540 310" aria-hidden="true">
    <defs>
      <clipPath id="front-disc"><circle cx="-30" cy="170" r="165"/></clipPath>
    </defs>
    <g clip-path="url(#front-disc)">
      <rect x="-200" y="0" width="400" height="310" fill="#c8962a"/>
      <rect x="-200" y="52" width="400" height="28" fill="#121212"/>
      <rect x="-200" y="112" width="400" height="28" fill="#121212"/>
      <rect x="-200" y="172" width="400" height="28" fill="#121212"/>
      <rect x="-200" y="232" width="400" height="28" fill="#121212"/>
    </g>
    <rect x="150" y="0" width="70" height="22" fill="#c8962a"/>
  </svg>

  <div class="brand"><span class="brand-dot"></span>Ranger's Premium</div>

  <span class="band-rule" style="top:142px"></span>
  <span class="band-rule" style="top:146px"></span>
  <div class="name-band">
    <div class="person-name">Mara Ellston</div>
    <div class="person-role">Director</div>
  </div>
  <span class="band-rule" style="top:212px"></span>
  <span class="band-rule" style="top:216px"></span>

  <ul class="contact">
    <li>1 800 555 0142<svg class="contact-icon" viewBox="0 0 12 12"><path d="M2 1h3l1 3-2 1a7 7 0 0 0 3 3l1-2 3 1v3c-5 1-10-4-9-9z"/></svg></li>
    <li>08 5550 0198<svg class="contact-icon" viewBox="0 0 12 12"><path d="M3 1h6v3H3zM1 5h10v4H9v2H3V9H1zM4 8v2h4V8z"/></svg></li>
    <li>hello@rangersfeed.com<svg class="contact-icon" viewBox="0 0 12 12"><path d="M1 3h10v7H1zM1.5 3.5 6 7l4.5-3.5" stroke="#121212" stroke-width="1"/></svg></li>
    <li>4/12 Mesa Road, Dry Creek, Town<svg class="contact-icon blank" viewBox="0 0 12 12"></svg></li>
    <li>TX 790, Dry Creek TX 790<svg class="contact-icon" viewBox="0 0 12 12"><path d="M6 0a4 4 0 0 0-4 4c0 3 4 8 4 8s4-5 4-8a4 4 0 0 0-4-4zm0 2.5a1.5 1.5 0 1 1 0 3 1.5 1.5 0 0 1 0-3z"/></svg></li>
  </ul>
</section>

<section class="card card-back" aria-label="Business card back">
  <svg class="card-art" viewBox="0 0 540 310" aria-hidden="true">
    <defs>
      <clipPath id="back-disc"><circle cx="560" cy="175" r="175"/></clipPath>
    </defs>
    <g clip-path="url(#back-disc)">
      <rect x="380" y="0" width="200" height="310" fill="#121212"/>
      <rect x="380" y="62" width="200" height="26" fill="#c8962a"/>
      <rect x="380" y="122" width="200" height="26" fill="#c8962a"/>
      <rect x="380" y="182" width="200" height="26" fill="#c8962a"/>
      <rect x="380" y="242" width="200" height="26" fill="#c8962a"/>
    </g>
  </svg>

  <div class="brand"><span class="brand-dot"></span>Ranger's Premium</div>
  <p class="tagline">Freshness is our FIRST Promise !</p>
</section>

</body>
</html>
```